Harborlight Behavioral and Community Services

Intellectual Developmental Disabilities, Group Homes, Residential Homes and Substance Abuse Residential facilities

Target Market(s)

Adults 18-59 male and female autism, developmental disabilities and mental health

Industry/Entity Type

Intellectual Development Disabilities, Autism, Applied Behavioral Analysis, Mental Health, Substance Abuse

Coding

Coded - Design and coding required

Number of Pages Required

5+ page

Font styles to use
Serif

Colors
0054AA
0677BA
7BADD7
CADEEF
E8F1F8

Requirements
Should not have
• Not specified

```html
<!DOCTYPE html>
<html lang="en">
<head>
<meta charset="utf-8">
<title>Behavioral and Community Services</title>
<link href="https://fonts.googleapis.com/css2?family=Poppins:wght@400;500;600;700&family=Open+Sans:wght@400;600&display=swap" rel="stylesheet">
<style>
:root{
  --blue-900:#0054AA;
  --blue-700:#0677BA;
  --blue-400:#7BADD7;
  --blue-200:#CADEEF;
  --blue-100:#E8F1F8;
  --navy:#0b1a33;
  --ink:#111827;
  --muted:#5b6472;
  --white:#ffffff;
}
*{box-sizing:border-box;margin:0;padding:0}
html,body{width:1200px;height:3628px;overflow:hidden}
body{font-family:"Open Sans",Arial,sans-serif;color:var(--ink);background:var(--white);position:relative}
h1,h2,h3,h4,.btn,.nav a,.logo{font-family:"Poppins",Arial,sans-serif}
section,header,footer{position:relative;width:1200px;overflow:hidden}
.btn{display:inline-block;font-size:11px;font-weight:500;padding:9px 16px;border-radius:2px;text-decoration:none}
.btn-solid{background:var(--blue-900);color:var(--white)}
.btn-outline{border:1px solid var(--blue-900);color:var(--blue-900);background:var(--white)}
.photo{position:absolute}

/* header */
.site-header{height:60px;display:flex;align-items:center;padding:0 150px}
.logo{font-weight:700;font-size:16px;color:var(--ink);letter-spacing:.3px}
.nav{margin-left:auto;display:flex;gap:20px;margin-right:40px}
.nav a{font-size:9px;font-weight:600;color:var(--ink);text-decoration:none;letter-spacing:.3px}
.site-header .btn{padding:7px 26px}

/* hero */
.hero{height:580px}
.hero-photo{left:640px;top:0;width:560px;height:580px;background:linear-gradient(160deg,#d9dde0 0%,#b7a48a 45%,#8a7560 100%)}
.hero-copy{position:absolute;left:150px;top:170px;width:450px}
.hero h1{font-size:30px;line-height:1.22;font-weight:700}
.hero p{font-size:11.5px;line-height:1.6;margin-top:14px;color:#222}
.hero-actions{margin-top:22px;display:flex;gap:8px}
.search-bar{margin-top:30px;display:flex;align-items:center;width:440px;height:44px;background:var(--white);box-shadow:0 4px 18px rgba(0,0,0,.1);padding:0 10px;gap:10px}
.search-field{flex:1;font-size:10px;color:var(--muted);display:flex;align-items:center;justify-content:space-between;padding:0 8px}
.search-bar .btn{padding:8px 24px;display:flex;gap:6px;align-items:center}

/* services */
.services{height:420px}
.section-title{font-size:34px;font-weight:700;text-align:center}
.services .section-title{position:absolute;top:50px;width:100%}
.service-card{position:absolute;width:390px;height:104px;background:var(--white);box-shadow:0 4px 20px rgba(0,0,0,.09);display:flex;align-items:center;gap:18px;padding:0 26px}
.service-card h3{font-size:13px;font-weight:600;line-height:1.3}
.service-card svg{flex:none}

/* about */
.about{height:420px}
.about-panel{position:absolute;left:150px;top:20px;width:462px;height:370px;background:var(--blue-700);color:var(--white);padding:126px 40px 0 60px}
.eyebrow{font-size:9px;letter-spacing:1.5px;font-weight:600;text-transform:uppercase}
.about-panel h2{font-size:32px;line-height:1.2;font-weight:700;margin-top:10px}
.about-copy{position:absolute;left:672px;top:28px;width:488px;font-size:11px;line-height:1.65;color:var(--muted)}
.about-copy p+p{margin-top:8px}
.about-copy .btn{margin-top:14px}

/* photo band */
.story-band{height:440px}
.story-photo{inset:0;background:linear-gradient(180deg,#d9c3a3 0%,#b8734f 35%,#a35b3f 70%,#8f8a7e 100%)}

/* join */
.join{height:568px;text-align:center}
.join .eyebrow{position:absolute;top:86px;left:0;width:100%;color:var(--muted);font-size:8px}
.join .section-title{position:absolute;top:104px;left:0;width:100%}
.join-lead{position:absolute;top:162px;left:320px;width:560px;font-size:11px;line-height:1.6;color:#333}
.join-card{position:absolute;top:240px;width:228px;text-align:left}
.join-card .photo{position:static;display:block;height:160px;width:100%}
.join-card h4{font-size:12px;font-weight:600;line-height:1.35;margin-top:14px}
.join-card a{display:block;font-size:10px;color:var(--ink);margin-top:4px;text-decoration:none}

/* reach */
.reach{height:360px;background:var(--blue-100)}
.reach-copy{position:absolute;left:160px;top:100px;width:320px}
.reach h2{font-size:22px;font-weight:700;line-height:1.25}
.reach-note{display:flex;gap:10px;margin-top:10px;font-size:10px;line-height:1.5;color:#333;align-items:flex-start}
.reach .btn{margin-top:18px}
.stats{position:absolute;left:560px;top:130px;display:flex;gap:46px}
.stat strong{display:block;font-family:"Poppins",sans-serif;font-size:34px;font-weight:700;line-height:1}
.stat span{display:block;font-size:9.5px;color:#333;margin-top:8px;text-align:center}

/* news */
.news{height:430px}
.news .section-title{position:absolute;top:62px;width:100%}
.news-card{position:absolute;top:112px;width:240px}
.news-card .photo{position:static;display:block;height:180px;width:100%}
.news-card h4{font-size:12px;font-weight:600;line-height:1.35;margin-top:14px}
.news-card a{display:block;font-size:10px;color:var(--ink);margin-top:10px;text-decoration:none}

/* footer */
.site-footer{height:350px;background:var(--navy);color:var(--white)}
.footer-col{position:absolute;top:100px}
.site-footer .logo{color:var(--white);font-size:22px}
.footer-about p{font-size:10.5px;line-height:1.5;margin-top:6px;width:230px;color:#d7dce4}
.footer-col h4{font-size:11px;font-weight:600;margin-bottom:10px}
.footer-col ul{list-style:none}
.footer-col li{font-size:9px;color:#cfd5de;line-height:1.8}
.footer-col li::before{content:"› ";color:var(--blue-400)}
.contact-row{display:flex;gap:8px;align-items:flex-start;font-size:9px;color:#cfd5de;margin-bottom:8px;line-height:1.5}
.subscribe p{font-size:9px;color:#cfd5de;width:180px;line-height:1.5}
.subscribe-form{display:flex;margin-top:10px;width:180px}
.subscribe-form span{flex:1;background:var(--white);color:var(--muted);font-size:8px;padding:7px 8px}
.subscribe-form b{background:var(--blue-900);width:28px;display:flex;align-items:center;justify-content:center}
.socials{display:flex;gap:5px;margin-top:10px}
.socials i{width:14px;height:14px;background:var(--white);display:block}
.copyright{position:absolute;bottom:0;width:100%;height:34px;border-top:1px solid rgba(255,255,255,.15);font-size:8px;text-align:center;line-height:34px;color:#aab3c0}
</style>
</head>
<body>

<header class="site-header">
  <div class="logo">LOGO HERE</div>
  <nav class="nav">
    <a href="#">ABOUT US</a><a href="#">OUR SERVICES</a><a href="#">PEER SUPPORT</a><a href="#">SUCCESS STORIES</a><a href="#">CAREERS</a>
  </nav>
  <a class="btn btn-outline" href="#">Donate</a>
</header>

<section class="hero">
  <div class="photo hero-photo" role="img" aria-label="Person in a wheelchair by the sea at sunset"></div>
  <div class="hero-copy">
    <h1>Empowering Lives,<br>Transforming Communities</h1>
    <p>We are committed to helping individuals with intellectual disabilities, autism, and mental health challenges lead fulfilling and independent lives.</p>
    <div class="hero-actions">
      <a class="btn btn-solid" href="#">Join Our Team</a>
      <a class="btn btn-outline" href="#">Donate Today</a>
    </div>
    <div class="search-bar">
      <div class="search-field">Select Service
        <svg width="8" height="5" viewBox="0 0 8 5"><path d="M0 0l4 5 4-5z" fill="#555"/></svg></div>
      <div class="search-field">Enter Zip Code</div>
      <a class="btn btn-solid" href="#"><svg width="10" height="10" viewBox="0 0 10 10"><circle cx="4" cy="4" r="3" fill="none" stroke="#fff" stroke-width="1.4"/><path d="M6.3 6.3L9.5 9.5" stroke="#fff" stroke-width="1.4"/></svg>Search</a>
    </div>
  </div>
</section>

<section class="services">
  <h2 class="section-title">Our Services</h2>
  <div class="service-card" style="left:210px;top:132px">
    <svg width="40" height="40" viewBox="0 0 40 40" fill="none" stroke="#0054AA" stroke-width="1.8"><circle cx="12" cy="11" r="4"/><circle cx="28" cy="11" r="4"/><circle cx="20" cy="19" r="3"/><path d="M5 34V22a7 7 0 0114 0M21 22a7 7 0 0114 0v12M15 34v-6a5 5 0 0110 0v6"/></svg>
    <h3>Comprehensive Support for<br>Every Stage of Life</h3>
  </div>
  <div class="service-card" style="left:615px;top:132px">
    <svg width="40" height="40" viewBox="0 0 40 40" fill="none" stroke="#0054AA" stroke-width="1.8"><path d="M12 36v-7c-4-3-6-7-6-11a13 13 0 0126 0l4 7h-4v5h-7v6"/><circle cx="19" cy="17" r="5"/></svg>
    <h3>Intellectual &amp; Developmental<br>Disabilities</h3>
  </div>
  <div class="service-card" style="left:210px;top:268px">
    <svg width="40" height="40" viewBox="0 0 40 40" fill="none" stroke="#0054AA" stroke-width="1.8"><circle cx="20" cy="9" r="4"/><path d="M4 16l8 10v10M36 16l-8 10v10M14 30h12"/><path d="M20 16v8"/></svg>
    <h3>Mental Health &amp; Behavioral<br>Therapy</h3>
  </div>
  <div class="service-card" style="left:615px;top:268px">
    <svg width="40" height="40" viewBox="0 0 40 40" fill="none" stroke="#0054AA" stroke-width="1.8"><path d="M8 36V22l6-4h10a3 3 0 010 6h-6M8 30h16l10-8a3 3 0 00-4-4l-6 4"/><path d="M22 6v8M18 10h8"/></svg>
    <h3>Substance Abuse<br>Recovery</h3>
  </div>
</section>

<section class="about">
  <div class="about-panel">
    <span class="eyebrow">Who We Are</span>
    <h2>A Community That Feels Like Home</h2>
  </div>
  <div class="about-copy">
    <p>For many years we have been a trusted provider of developmental and behavioral health services, offering support that goes beyond care. At our core, we believe that every individual deserves respect, dignity, and the right to thrive in their community. Our expert team is dedicated to providing personalized programs that address intellectual disabilities, autism spectrum disorders, and behavioral health needs.</p>
    <p>Whether it's helping someone develop daily living skills, find meaningful employment, or access clinical mental health support, we reaffirm our commitment to empower, educate, and uplift.</p>
    <a class="btn btn-solid" href="#">Read More</a>
  </div>
</section>

<section class="story-band">
  <div class="photo story-photo" role="img" aria-label="Child pushing a friend in a wheelchair past a brick wall"></div>
</section>

<section class="join">
  <span class="eyebrow">Get Involved</span>
  <h2 class="section-title">Join Us in Making a Difference</h2>
  <p class="join-lead">Every individual deserves the chance to reach their full potential, and you can be a part of that change. Whether you choose to join our dedicated team, volunteer your time, or donate, your support plays a crucial role in shaping lives and strengthening communities.</p>
  <div class="join-card" style="left:232px">
    <div class="photo" role="img" aria-label="Caregiver sitting with a young man at a table" style="background:linear-gradient(160deg,#d8d2c8,#9c8d7c)"></div>
    <h4>Looking for a<br>Meaningful Career?</h4><a href="#">Apply Now</a>
  </div>
  <div class="join-card" style="left:484px">
    <div class="photo" role="img" aria-label="Group activity at a community program" style="background:linear-gradient(160deg,#c9d3de,#8d9fb4)"></div>
    <h4>Support Life-<br>Changing Programs</h4><a href="#">Donate Now</a>
  </div>
  <div class="join-card" style="left:734px">
    <div class="photo" role="img" aria-label="Family smiling together at home" style="background:linear-gradient(160deg,#c98a6c,#7d4a3a)"></div>
    <h4>Stay Connected<br>&amp; Get Updates</h4><a href="#">Sign Up for Our Newsletter</a>
  </div>
</section>

<section class="reach">
  <div class="reach-copy">
    <h2>Explore Our Reach<br>Across the Country</h2>
    <div class="reach-note">
      <svg width="22" height="22" viewBox="0 0 22 22" fill="none" stroke="#0054AA" stroke-width="1.6"><path d="M11 20s-7-6-7-11a7 7 0 0114 0c0 5-7 11-7 11z"/><circle cx="11" cy="9" r="2.5"/></svg>
      <span>See how we're making a difference in<br>your community!</span>
    </div>
    <a class="btn btn-solid" href="#">Find Services Near You</a>
  </div>
  <div class="stats">
    <div class="stat"><strong>30,000+</strong><span>Lives Changed Annually</span></div>
    <div class="stat"><strong>660+</strong><span>Locations Nationwide</span></div>
    <div class="stat"><strong>12</strong><span>States &amp; Growing</span></div>
  </div>
</section>

<section class="news">
  <h2 class="section-title">Latest News &amp; Events</h2>
  <div class="news-card" style="left:228px">
    <div class="photo" role="img" aria-label="Children playing at a community event" style="background:linear-gradient(160deg,#c7b59a,#6f7f92)"></div>
    <h4>Upcoming Events &amp;<br>Community Highlights</h4><a href="#">Read More</a>
  </div>
  <div class="news-card" style="left:480px">
    <div class="photo" role="img" aria-label="Bowling alley lanes" style="background:linear-gradient(160deg,#2c3a55,#9a6a48)"></div>
    <h4>2025 Bowling Tournament<br>– Save the Date!</h4><a href="#">Read More</a>
  </div>
  <div class="news-card" style="left:732px">
    <div class="photo" role="img" aria-label="Parents and children talking together" style="background:linear-gradient(160deg,#d9c9b5,#8a6e5a)"></div>
    <h4>Networking Events for<br>Children &amp; Family Services</h4><a href="#">Read More</a>
  </div>
</section>

<footer class="site-footer">
  <div class="footer-col footer-about" style="left:150px">
    <div class="logo">LOGO HERE</div>
    <p>Lorem Ipsum is simply dummy text of the printing and typesetting industry. Lorem Ipsum has been the</p>
  </div>
  <div class="footer-col" style="left:470px">
    <h4>Information</h4>
    <ul><li>Home</li><li>About Us</li><li>Our Services</li><li>Peer Support</li><li>Success Stories</li><li>Careers</li><li>Contact</li></ul>
  </div>
  <div class="footer-col" style="left:640px">
    <h4>Contact Us</h4>
    <div class="contact-row"><svg width="10" height="10" viewBox="0 0 10 10"><path d="M2 1l2 2-1 1.5a6 6 0 002.5 2.5L7 6l2 2-1.5 1.5C4 9 1 6 .5 2.5z" fill="#7BADD7"/></svg>(555) 014-2280</div>
    <div class="contact-row"><svg width="10" height="10" viewBox="0 0 10 10"><rect x=".5" y="2" width="9" height="6" fill="none" stroke="#7BADD7"/><path d="M.5 2l4.5 3.5L9.5 2" fill="none" stroke="#7BADD7"/></svg>hello@tidewaycare.example</div>
    <div class="contact-row"><svg width="10" height="10" viewBox="0 0 10 10"><path d="M5 9.5S1.5 6.5 1.5 4a3.5 3.5 0 017 0c0 2.5-3.5 5.5-3.5 5.5z" fill="#7BADD7"/></svg>Tidal Grove 42<br>Maplehaven<br>ST 10024 Place</div>
  </div>
  <div class="footer-col subscribe" style="left:855px">
    <h4>Subscribe Newsletter</h4>
    <p>Subscribe our newsletter for the latest offers updates</p>
    <div class="subscribe-form"><span>Enter Email</span><b><svg width="10" height="8" viewBox="0 0 10 8"><path d="M0 4h8M5 1l3 3-3 3" stroke="#fff" fill="none" stroke-width="1.3"/></svg></b></div>
    <div class="socials"><i></i><i></i><i></i><i></i></div>
  </div>
  <div class="copyright">2025 Copyright © All Rights Reserved</div>
</footer>

</body>
</html>
```